Glaze Me is a high end dessert topping line made with all natural ingredients and no preservatives. The initial flavor is fudge with more flavors to follow such as peppermint, salted caamel etc. My target market will be specialty food stores. I will be selling my product in 9 oz and 4 oz straight sided jars. I am open to all ideas but am leaning toward a more upscale, sophisticated look with colors/design that will stand out on a shelf. I want the flavor of the topping to feature prominently in the design so the product is readily identifiable to the consumer. I also need room for nutritional facts.

```html
<!DOCTYPE html>
<html lang="en">
<head>
<meta charset="utf-8">
<title>Glaze Me – Label Concepts</title>
<link rel="stylesheet" href="https://fonts.googleapis.com/css2?family=Jost:wght@400;500&display=swap">
<style>
  :root {
    --page-bg: #ffffff;
    --cream: #e5e2c7;
    --charcoal: #58585a;
    --ink: #111111;
    --white: #ffffff;
    --fudge: #7d6650;
    --fudge-light: #9a846c;
    --caramel: #fbb531;
    --caramel-light: #fdd27a;
    --pistachio: #8f8a4c;
    --pistachio-light: #aca872;
    --orange: #f26f55;
    --orange-light: #f7a08a;
  }
  * { box-sizing: border-box; margin: 0; padding: 0; }
  html, body { width: 1200px; height: 1000px; overflow: hidden; background: var(--page-bg); }
  body { position: relative; font-family: "Jost", sans-serif; }

  .label {
    position: absolute;
    width: 20.75em;
    height: 27em;
    font-size: 16px;
  }
  .label--sample { font-size: 10.66px; }

  .label__pattern {
    position: absolute; inset: 0;
    background: linear-gradient(90deg, var(--tone), var(--tone-light) 50%, var(--tone));
  }
  .label--fudge { --tone: var(--fudge); --tone-light: var(--fudge-light); --accent: var(--fudge); }
  .label--caramel { --tone: var(--caramel); --tone-light: var(--caramel-light); --accent: var(--caramel); }
  .label--pistachio { --tone: var(--pistachio); --tone-light: var(--pistachio-light); --accent: var(--pistachio); }
  .label--orange { --tone: var(--orange); --tone-light: var(--orange-light); --accent: var(--orange); }

  .label__brand-panel {
    position: absolute;
    left: 2.69em; top: 2.94em;
    width: 15.375em; height: 14.625em;
    background: var(--cream);
  }
  .brand__dot {
    position: absolute;
    left: 50%; top: 2.3em;
    width: 3.9em; height: 3.9em;
    margin-left: -1.95em;
    border-radius: 50%;
    background: var(--accent);
  }
  .brand__name {
    position: absolute;
    left: 0; right: 0; top: 3.1em;
    text-align: center;
    font-size: 2.75em;
    font-weight: 500;
    line-height: 1;
    letter-spacing: 0.02em;
    white-space: nowrap;
    color: var(--charcoal);
  }
  .brand__tagline {
    position: absolute;
    left: 0; right: 0; top: 15.5em;
    text-align: center;
    font-size: 0.82em;
    font-weight: 500;
    line-height: 1;
    white-space: nowrap;
    color: var(--charcoal);
  }

  .label__flavour {
    position: absolute;
    left: 2.69em; top: 19em;
    width: 15.375em; height: 5em;
    background: var(--charcoal);
    display: flex; align-items: center; justify-content: center;
  }
  .flavour__name {
    font-size: 1.5em;
    font-weight: 500;
    letter-spacing: 0.22em;
    padding-left: 0.22em;
    color: var(--white);
  }

  .samples__caption {
    position: absolute;
    left: 0; width: 1200px; top: 590px;
    text-align: center;
    font-size: 16px;
    font-weight: 500;
    letter-spacing: 0.3em;
    color: var(--ink);
  }
</style>
</head>
<body>
  <section class="label label--fudge" style="left:434px; top:100px;">
    <div class="label__pattern" role="img" aria-label="Vertical wavy stripe pattern in fudge brown, cream and charcoal"></div>
    <div class="label__brand-panel">
      <span class="brand__dot"></span>
      <p class="brand__name">GLAZE ME</p>
      <p class="brand__tagline">GOURMET DESSERT TOPPING</p>
    </div>
    <div class="label__flavour"><span class="flavour__name">HOT FUDGE</span></div>
  </section>

  <p class="samples__caption">SAMPLE COLORS FOR FLAVOURS</p>

  <section class="label label--sample label--caramel" style="left:200px; top:632px;">
    <div class="label__pattern" role="img" aria-label="Vertical wavy stripe pattern in caramel yellow, cream and charcoal"></div>
    <div class="label__brand-panel">
      <span class="brand__dot"></span>
      <p class="brand__name">GLAZE ME</p>
      <p class="brand__tagline">GOURMET DESSERT TOPPING</p>
    </div>
    <div class="label__flavour"><span class="flavour__name">CARAMEL</span></div>
  </section>

  <section class="label label--sample label--pistachio" style="left:489px; top:632px;">
    <div class="label__pattern" role="img" aria-label="Vertical wavy stripe pattern in pistachio green, cream and charcoal"></div>
    <div class="label__brand-panel">
      <span class="brand__dot"></span>
      <p class="brand__name">GLAZE ME</p>
      <p class="brand__tagline">GOURMET DESSERT TOPPING</p>
    </div>
    <div class="label__flavour"><span class="flavour__name">PISTACCIO</span></div>
  </section>

  <section class="label label--sample label--orange" style="left:780px; top:632px;">
    <div class="label__pattern" role="img" aria-label="Vertical wavy stripe pattern in orange, cream and charcoal"></div>
    <div class="label__brand-panel">
      <span class="brand__dot"></span>
      <p class="brand__name">GLAZE ME</p>
      <p class="brand__tagline">GOURMET DESSERT TOPPING</p>
    </div>
    <div class="label__flavour"><span class="flavour__name">ORANGE</span></div>
  </section>
</body>
</html>
```